Business Card for a Mortgage Agent (myself)

I need a business card for my new job as Mortgage Agent. The Broker's logo is to be on the card as well as the brokerage License number. Not sure if to include a photo or not. Info to be on card.
Dante Roux
Mortgage Agent
Lic # M47105386
Cell: 905-614-2753
Email: danterouxk.ma@fennmail.com
Web: www.karlvostermortgages.com
TPW Brokerage Lic. # 73918

```html
<!DOCTYPE html>
<html lang="en">
<head>
<meta charset="utf-8">
<title>Dante Roux – Mortgage Agent Business Card</title>
<link rel="stylesheet" href="https://fonts.googleapis.com/css2?family=Arimo:ital,wght@0,400;0,700;1,700&family=Playfair+Display:wght@500&family=Questrial&display=swap">
<style>
  :root {
    --page-bg: #b4b7ba;
    --navy: #1b2a5e;
    --navy-deep: #132253;
    --skyline: #23407e;
    --brand-blue: #1656a6;
    --brand-yellow: #f7c51e;
    --ink: #222a35;
    --white: #ffffff;
    --photo-light: #f3f4f5;
    --photo-mid: #c9ccd1;
    --photo-dark: #3b3f46;
  }
  * { box-sizing: border-box; margin: 0; padding: 0; }
  html, body { width: 1187px; height: 1200px; overflow: hidden; }
  body { background: var(--page-bg); position: relative; font-family: "Arimo", Arial, sans-serif; }

  .card {
    position: absolute;
    left: 214px;
    width: 760px;
    height: 434px;
    border-radius: 18px;
    overflow: hidden;
  }

  /* Front */
  .card-front {
    top: 122px;
    background: radial-gradient(ellipse at 50% 40%, #22306a 0%, var(--navy) 60%, var(--navy-deep) 100%);
    color: var(--white);
  }
  .front-name {
    position: absolute;
    top: 168px;
    left: 0; right: 0;
    text-align: center;
    font-family: "Questrial", "Helvetica Neue", sans-serif;
    font-weight: 400;
    font-size: 54px;
    line-height: 1;
    letter-spacing: 0.02em;
  }
  .front-title {
    position: absolute;
    top: 236px;
    left: 0; right: 0;
    text-align: center;
    font-family: "Arimo", Arial, sans-serif;
    font-size: 18px;
    letter-spacing: 0.78em;
    padding-left: 0.78em;
  }
  .front-skyline {
    position: absolute;
    left: 0; right: 0; bottom: 0;
    height: 132px;
    background: linear-gradient(180deg, rgba(35,64,126,0) 0%, rgba(35,64,126,0.65) 35%, var(--skyline) 100%);
  }

  /* Back */
  .card-back {
    top: 643px;
    background: var(--white);
    color: var(--ink);
  }
  .back-photo {
    position: absolute;
    left: 332px; right: 0; top: 23px; bottom: 13px;
    background: radial-gradient(ellipse at 62% 38%, var(--photo-mid) 0%, var(--photo-light) 55%),
                linear-gradient(160deg, var(--photo-light) 40%, var(--photo-dark) 100%);
    background-blend-mode: multiply;
  }
  .agent {
    position: absolute;
    left: 52px;
    top: 38px;
  }
  .agent-name {
    font-family: "Playfair Display", Georgia, serif;
    font-weight: 500;
    font-size: 33px;
    line-height: 1;
    color: var(--brand-blue);
    transform: scaleX(0.86);
    transform-origin: left center;
  }
  .agent-role, .agent-licence {
    font-size: 17px;
    letter-spacing: 0.06em;
    line-height: 1;
    color: var(--ink);
  }
  .agent-role { margin-top: 11px; }
  .agent-licence { margin-top: 12px; }
  .divider {
    width: 150px;
    height: 1px;
    background: var(--brand-blue);
    margin-top: 10px;
  }
  .contacts { list-style: none; margin-top: 14px; }
  .contacts li {
    display: flex;
    align-items: center;
    gap: 8px;
    font-size: 17px;
    letter-spacing: 0.04em;
    line-height: 1;
    height: 33px;
    white-space: nowrap;
  }
  .contacts svg { width: 15px; height: 15px; flex: none; fill: var(--brand-blue); }

  .broker {
    position: absolute;
    left: 52px;
    top: 252px;
    width: 212px;
  }
  .broker-name {
    display: flex;
    align-items: center;
    justify-content: center;
    height: 118px;
    font-family: "Arimo", Arial, sans-serif;
    font-weight: 700;
    font-size: 24px;
    color: var(--brand-blue);
    white-space: nowrap;
  }
  .broker-licence {
    margin-top: 12px;
    font-weight: 700;
    font-style: italic;
    font-size: 15px;
    color: var(--brand-blue);
    white-space: nowrap;
  }

  .stripe-blue, .stripe-yellow { position: absolute; left: 0; right: 0; }
  .stripe-blue { bottom: 8px; height: 5px; background: var(--brand-blue); }
  .stripe-yellow { bottom: 0; height: 8px; background: var(--brand-yellow); }
</style>
</head>
<body>

  <section class="card card-front">
    <h1 class="front-name">DANTE ROUX</h1>
    <p class="front-title">MORTGAGE AGENT</p>
    <div class="front-skyline" role="img" aria-label="City skyline silhouette in dark blue along the bottom of the card"></div>
  </section>

  <section class="card card-back">
    <div class="back-photo" role="img" aria-label="Portrait photo of the agent in a dark suit, shirt and tie"></div>

    <div class="agent">
      <h2 class="agent-name">DANTE ROUX</h2>
      <p class="agent-role">Mortgage Agent</p>
      <p class="agent-licence">Lic # M47105386</p>
      <div class="divider"></div>
      <ul class="contacts">
        <li>
          <svg viewBox="0 0 16 16" aria-hidden="true"><path d="M3.6 1.2l2.3 2.5-1.2 1.9c.8 1.9 2.2 3.4 4.1 4.3l1.9-1.2 2.6 2.3-1 2.6C8.5 14 2 8 1.1 2.3z"/></svg>
          <span>(905) 614-2753</span>
        </li>
        <li>
          <svg viewBox="0 0 16 16" aria-hidden="true"><path d="M1 3h14v1.6L8 9 1 4.6z"/><path d="M1 6.2l7 4.4 7-4.4V13H1z"/></svg>
          <span>danterouxk.ma@fennmail.com</span>
        </li>
        <li>
          <svg viewBox="0 0 16 16" aria-hidden="true"><path d="M8 1a7 7 0 100 14A7 7 0 008 1zm-.6 2.2c.4 1-.6 1.3-1.2 2-.5.6.5 1.2 1.4 1.4 1 .2 1.2 1.3.5 2-.6.6-.2 1.6-.3 2.6-1.6-.3-1.8-2.2-2.6-3.2-.6-.8-1.8-.6-2.3-1.3.6-1.8 2.5-3.3 4.5-3.5zm3.8 1.3c1.5 1.1 2.2 2.8 2 4.6-.7-.4-1.2-1.3-2-1.5-.7-.3-1.3-1-.8-1.6.5-.5.7-1 .8-1.5z"/></svg>
          <span>www.karlvostermortgages.com</span>
        </li>
      </ul>
    </div>

    <div class="broker">
      <p class="broker-name">Tri-Point Wealth</p>
      <p class="broker-licence">TPW Brokerage Lic. # 73918</p>
    </div>

    <div class="stripe-blue"></div>
    <div class="stripe-yellow"></div>
  </section>

</body>
</html>
```